Property Report

8 page document, similar theme to our website (www.harbourandmeadows.com) and previous brochure (provided). All content provided. We want a professional looking document. We need ASAP. Thanks!

Industry/Entity Type

Property

Font styles to use
Serif
Sans Serif

Colors
ffc214
ffcf3e
fee18a
fff3d1

Requirements
Must have
• Page 1: Cover
Page 2: Content
Page 3: About Us
Page 4: Site Description
Page 5: Scheme
Page 6: Analysis
Page 7: Conclusion
Page 8: Contact Details

```html
<!DOCTYPE html>
<html lang="en">
<head>
<meta charset="utf-8">
<title>Contact Us – Harbour &amp; Meadows Commercial</title>
<link rel="stylesheet" href="https://fonts.googleapis.com/css2?family=Antonio:wght@400&family=Carlito:wght@400;700&display=swap">
<style>
  :root {
    --gold: #ffc214;
    --panel: #4c4d4f;
    --white: #ffffff;
    --photo-top: #a7a9ae;
    --photo-bottom: #c8c9cd;
  }
  * { margin: 0; padding: 0; box-sizing: border-box; }
  html, body { width: 848px; height: 1200px; overflow: hidden; background: var(--panel); }
  .page {
    position: relative;
    width: 848px;
    height: 1200px;
    background: var(--panel);
    font-family: "Carlito", "Calibri", sans-serif;
    color: var(--white);
    overflow: hidden;
  }
  .hero {
    position: absolute;
    inset: 0 0 auto 0;
    height: 600px;
  }
  .hero-photo {
    position: absolute;
    inset: 0;
    background: linear-gradient(180deg, var(--photo-top) 0%, var(--photo-bottom) 100%);
  }
  .hero-title {
    position: absolute;
    top: 275px;
    left: 0;
    width: 100%;
    text-align: center;
    font-family: "Antonio", "Oswald", sans-serif;
    font-weight: 400;
    font-size: 95px;
    line-height: 1;
    letter-spacing: 2px;
    color: var(--gold);
  }
  .contact {
    position: absolute;
    top: 600px;
    left: 0;
    width: 100%;
    text-align: center;
  }
  .company-name {
    margin-top: 29px;
    font-weight: 700;
    font-size: 28.5px;
    line-height: 1;
    color: var(--gold);
  }
  .address {
    margin-top: 10px;
    font-style: normal;
    font-size: 23px;
    line-height: 27.5px;
  }
  .phone {
    margin-top: 34px;
    font-weight: 700;
    font-size: 43px;
    line-height: 1;
    color: var(--gold);
  }
  .email, .web {
    font-size: 25px;
    line-height: 34px;
  }
  .email { margin-top: 2px; }
  .brand-name {
    position: absolute;
    top: 962px;
    left: 0;
    width: 100%;
    text-align: center;
    font-weight: 700;
    font-size: 62px;
    line-height: 69px;
    color: var(--white);
  }
</style>
</head>
<body>
  <main class="page">
    <section class="hero">
      <div class="hero-photo" role="img" aria-label="Photograph of two business people at a desk in a bright office, signing a document"></div>
      <h1 class="hero-title">Contact Us</h1>
    </section>

    <section class="contact">
      <h2 class="company-name">Harbour &amp; Meadows Commercial</h2>
      <address class="address">
        Unit 4<br>
        17 Larkfield Lane<br>
        London<br>
        SE9 2QT
      </address>
      <p class="phone">020 7946 0321</p>
      <p class="email">info@harbourandmeadows.com</p>
      <p class="web">www.harbourandmeadows.com</p>
    </section>

    <p class="brand-name">Harbour &amp;<br>Meadows<br>Commercial</p>
  </main>
</body>
</html>
```